ARC VOLLEY Business Card Project

I'd like to request a business card design for the new company I've launched.
The name of the company is "ARC VOLLEY" an indoor unmanned tennis practice facility.
We would like to see designs that use our brand identity color in the logo I've attached.
We hope to get the design with modern, luxurious and elegant tone and manner.
We hope the logo should not be too big.

Business card must have elements as below:
- Logo (One of the logos I've attached)
- Name (In Korean Text) : 박 서 윤
- Title (In Korean Text) : 대표
- Phone Number : 010-8472-3916
- Email Address : seoyun.park@arcvolley-example.co.kr
- Website : www.arcvolley-example.co.kr
- Instagram : arcvolley
- Address (In Korean text) : 경기도 용인시 수지구 풍덕천로 456 미래타워 5층 501호, 502호

Target Market(s)

Tennis amateurs in 20 to 40s

Industry/Entity Type

Sports, Hobby

Contact Information for Business Card

- Logo (One of the logos I've attached) - Name (In Korean Text) : 박 서 윤 - Title (In Korean Text) : 대표 - Phone Number : 010-8472-3916 - Email Address : seoyun.park@arcvolley-example.co.kr - Website : www.arcvolley-example.co.kr - Instagram : arcvolley - Address (In Korean text) : 경기도 용인시 수지구 풍덕천로 456 미래타워 5층 501호, 502호

Font styles to use
Sans Serif

Requirements
Must have
• Double sided
Nice to have
• Logo with intaglio or relief embossing
Should not have
• Logo should not be too big.

```html
<!DOCTYPE html>
<html lang="ko">
<head>
<meta charset="utf-8">
<title>ARC VOLLEY Business Card</title>
<link href="https://fonts.googleapis.com/css2?family=Noto+Sans+KR:wght@400;500;700&display=swap" rel="stylesheet">
<style>
  :root {
    --page: #2b2b2d;
    --card-dark: #3b3b3d;
    --card-dark-pattern: #333335;
    --card-light: #ffffff;
    --brand-green: #24533a;
    --ink: #2a2a2a;
    --faint: #eceeec;
    --on-dark: #ffffff;
  }
  * { box-sizing: border-box; margin: 0; padding: 0; }
  html, body { width: 1200px; height: 939px; overflow: hidden; }
  body {
    background: var(--page);
    font-family: "Noto Sans KR", sans-serif;
    position: relative;
  }
  .card {
    position: absolute;
    width: 620px;
    height: 344px;
    border-radius: 4px;
    overflow: hidden;
    box-shadow: 0 12px 30px rgba(0,0,0,.45);
  }
  /* Back side */
  .card-back { left: 130px; top: 90px; background: var(--card-dark); }
  .card-back .pattern {
    position: absolute; inset: 0;
    background: linear-gradient(135deg, var(--card-dark-pattern), var(--card-dark) 60%, #444446);
  }
  .card-back .brand {
    position: absolute; left: 0; right: 0; top: 50%;
    transform: translateY(-50%);
    display: flex; flex-direction: column; align-items: center; gap: 14px;
  }
  .card-back .brand-dot {
    width: 54px; height: 54px; border-radius: 50%;
    background: var(--on-dark);
  }
  .card-back .brand-name {
    color: var(--on-dark); font-size: 30px; font-weight: 500; letter-spacing: 2px;
  }
  /* Front side */
  .card-front { left: 450px; top: 500px; background: var(--card-light); color: var(--ink); }
  .card-front .faint-mark {
    position: absolute; right: 40px; top: -60px;
    width: 220px; height: 220px; border-radius: 50%;
    border: 10px solid var(--faint);
  }
  .front-logo {
    position: absolute; left: 34px; top: 56px;
    display: flex; align-items: center; gap: 14px;
  }
  .front-logo .brand-dot {
    width: 58px; height: 58px; border-radius: 50%; background: var(--brand-green);
  }
  .front-logo .brand-name {
    color: var(--brand-green); font-size: 30px; font-weight: 500; letter-spacing: 2px;
  }
  .rule { position: absolute; height: 2px; background: var(--brand-green); }
  .rule-top { left: 34px; right: 34px; top: 140px; }
  .instagram {
    position: absolute; right: 34px; top: 112px;
    display: flex; align-items: center; gap: 6px; font-size: 13px;
  }
  .instagram .handle-icon { width: 14px; height: 14px; border-radius: 50%; background: var(--brand-green); }
  .person { position: absolute; left: 34px; top: 160px; }
  .person .name { color: var(--brand-green); font-size: 30px; font-weight: 700; letter-spacing: 4px; line-height: 1.1; }
  .person .title { font-size: 14px; margin-top: 4px; }
  .rule-mid { left: 34px; width: 300px; top: 230px; height: 1px; }
  .contacts { position: absolute; left: 34px; top: 240px; list-style: none; font-size: 13px; line-height: 23px; }
  .contacts li { display: flex; align-items: center; gap: 8px; }
  .contacts .phone { letter-spacing: 3px; }
  .contacts svg { width: 13px; height: 13px; fill: var(--brand-green); flex: none; }
</style>
</head>
<body>

<section class="card card-back" aria-label="Card back">
  <div class="pattern" role="img" aria-label="Repeating embossed brand pattern in dark grey"></div>
  <div class="brand">
    <span class="brand-dot"></span>
    <span class="brand-name">ARC VOLLEY</span>
  </div>
</section>

<section class="card card-front" aria-label="Card front">
  <div class="faint-mark"></div>
  <div class="front-logo">
    <span class="brand-dot"></span>
    <span class="brand-name">ARC VOLLEY</span>
  </div>
  <div class="instagram"><span class="handle-icon"></span>arcvolley</div>
  <div class="rule rule-top"></div>

  <div class="person">
    <div class="name">박 서 윤</div>
    <div class="title">대표</div>
  </div>
  <div class="rule rule-mid"></div>

  <ul class="contacts">
    <li class="phone">
      <svg viewBox="0 0 24 24"><path d="M6.6 10.8a15 15 0 0 0 6.6 6.6l2.2-2.2c.3-.3.7-.4 1-.2 1.1.4 2.3.6 3.6.6.6 0 1 .4 1 1V20c0 .6-.4 1-1 1C10.6 21 3 13.4 3 4c0-.6.4-1 1-1h3.5c.6 0 1 .4 1 1 0 1.3.2 2.5.6 3.6.1.3 0 .7-.2 1z"/></svg>
      010-8472-3916
    </li>
    <li>
      <svg viewBox="0 0 24 24"><path d="M2 5h20v14H2z M3 6l9 7 9-7" fill="none" stroke="#24533a" stroke-width="2"/><path d="M2 5h20L12 12z"/></svg>
      seoyun.park@arcvolley-example.co.kr
    </li>
    <li>
      <svg viewBox="0 0 24 24"><circle cx="12" cy="12" r="9" fill="none" stroke="#24533a" stroke-width="2"/><path d="M3 12h18M12 3c3 3 3 15 0 18M12 3c-3 3-3 15 0 18" fill="none" stroke="#24533a" stroke-width="1.6"/></svg>
      www.arcvolley-example.co.kr
    </li>
    <li>
      <svg viewBox="0 0 24 24"><path d="M12 2a7 7 0 0 0-7 7c0 5 7 13 7 13s7-8 7-13a7 7 0 0 0-7-7zm0 9.5A2.5 2.5 0 1 1 12 6.5a2.5 2.5 0 0 1 0 5z"/></svg>
      경기도 용인시 수지구 풍덕천로 456 미래타워 5층 501호, 502호
    </li>
  </ul>
</section>

</body>
</html>
```